Product Image Design: Claiming the Salary You Deserve at Last (Plus Bonus!)

I need a product image designed for a new product I will be selling on sellvantrix.com that teaches how to quickly make more money by getting a raise or promotion.

Dimensions must be 1280 x 720 pixels. The product title and subtitle are as follows:

Title: Claiming the Full Salary You Deserve at Last (Plus Bonus!)

Subtitle: The Quickest Route toward a Huge Pay Bump Minus Costly Schooling Plus Flattering of Management

I'm looking for a design that is eye catching and communicates the idea of business success and getting paid more money from a company or employer.

The target audience is professional men in their 20s and 30s who are looking to quickly make more money and advance in their careers.

Target Market(s)

Professional men in their 20s and 30s who are looking to quickly make more money and advance in their careers.

Industry/Entity Type

Professional Service

Font styles to use
Serif

Requirements
Must have
• Title and subtitle provided in project description.

Final design in 1280 x 720 dimensions (or larger with same width to height ratio).

Eye catching font, colors and graphics, but not overly flashy.

Masculine colors (i.e. no pinks or other feminine colors).
Nice to have
• N/A
Should not have
• Feminine colors or images of women.

```html
<!DOCTYPE html>
<html lang="en">
<head>
<meta charset="utf-8">
<title>Claiming the Full Salary You Deserve at Last (Plus Bonus!)</title>
<link rel="stylesheet" href="https://fonts.googleapis.com/css2?family=Montserrat:wght@800;900&family=Oswald:wght@500;700&display=swap">
<style>
  :root {
    --bg-deep: #05080b;
    --bg-teal: #0c2a33;
    --bg-teal-soft: #15505c;
    --accent: #2ec2e3;
    --ink: #ffffff;
    --ink-soft: #e7f2f6;
    --photo-light: #55657f;
    --photo-mid: #35425a;
    --photo-dark: #1f2838;
  }
  html, body {
    margin: 0;
    padding: 0;
    overflow: hidden;
    background: var(--bg-deep);
  }
  .product-card {
    position: relative;
    width: 1200px;
    height: 675px;
    overflow: hidden;
    background: linear-gradient(115deg, var(--bg-teal) 0%, #0a1d24 40%, var(--bg-deep) 62%, #000 100%);
  }
  .backdrop {
    position: absolute;
    inset: 0;
  }
  .hero-photo {
    position: absolute;
    left: 656px;
    top: 18px;
    width: 544px;
    height: 657px;
    background: linear-gradient(160deg, var(--photo-light) 0%, var(--photo-mid) 45%, var(--photo-dark) 100%);
    clip-path: polygon(38% 0%, 62% 0%, 66% 30%, 86% 36%, 92% 27%, 100% 28%, 100% 100%, 4% 100%, 0% 80%, 8% 40%, 30% 32%, 34% 20%);
  }
  .headline {
    position: absolute;
    left: 30px;
    top: 78px;
    width: 780px;
    margin: 0;
    text-align: center;
    font-family: "Montserrat", sans-serif;
    font-weight: 900;
    color: var(--ink);
    text-transform: uppercase;
    line-height: 1;
    white-space: nowrap;
  }
  .headline-line {
    display: block;
  }
  .headline-top {
    font-size: 68px;
    letter-spacing: 0.5px;
  }
  .headline-mid {
    margin-top: 12px;
    font-size: 42px;
  }
  .highlight {
    display: inline-block;
    background: var(--accent);
    color: var(--ink);
    padding: 20px 10px 18px;
  }
  .headline-bonus {
    margin-top: 22px;
    font-size: 40px;
    color: var(--accent);
  }
  .divider {
    position: absolute;
    left: 98px;
    top: 336px;
    width: 564px;
    height: 60px;
  }
  .subtitle {
    position: absolute;
    left: 50px;
    top: 428px;
    width: 680px;
    margin: 0;
    text-align: center;
    font-family: "Oswald", sans-serif;
    font-weight: 500;
    font-size: 29px;
    line-height: 45px;
    color: var(--ink-soft);
  }
  .subtitle strong {
    font-weight: 700;
    text-transform: uppercase;
  }
</style>
</head>
<body>
  <main class="product-card">
    <svg class="backdrop" viewBox="0 0 1200 675" aria-hidden="true">
      <path d="M0 0 H380 L250 675 H0 Z" fill="var(--bg-teal-soft)" opacity="0.3"/>
      <path d="M700 0 H880 L800 675 H660 Z" fill="var(--bg-teal-soft)" opacity="0.55"/>
      <path d="M980 60 L1080 120 L1040 675 H940 Z" fill="var(--bg-teal-soft)" opacity="0.35"/>
    </svg>

    <div class="hero-photo" role="img" aria-label="Excited young man in a plaid shirt holding a fan of cash and raising his fist"></div>

    <h1 class="headline">
      <span class="headline-line headline-top">Claiming the Full</span>
      <span class="headline-line headline-mid"><span class="highlight">Salary</span> You <span class="highlight">Deserve</span> at Last</span>
      <span class="headline-line headline-bonus">(Plus Bonus!)</span>
    </h1>

    <svg class="divider" viewBox="0 0 564 60" aria-hidden="true">
      <line x1="0" y1="30" x2="254" y2="30" stroke="var(--accent)" stroke-width="2"/>
      <line x1="330" y1="30" x2="564" y2="30" stroke="var(--accent)" stroke-width="2"/>
      <g fill="none" stroke="var(--accent)" stroke-width="2.5">
        <ellipse cx="278" cy="12" rx="12" ry="4"/>
        <path d="M266 12 V40 A12 4 0 0 0 290 40 V12"/>
        <path d="M266 21 A12 4 0 0 0 290 21 M266 30 A12 4 0 0 0 290 30"/>
        <circle cx="302" cy="36" r="14" fill="var(--bg-deep)"/>
      </g>
      <text x="302" y="43" text-anchor="middle" font-family="Oswald, sans-serif" font-weight="700" font-size="19" fill="var(--accent)">$</text>
    </svg>

    <p class="subtitle">
      <strong>The Quickest Route</strong> toward a Huge Pay Bump<br>
      Minus Costly Schooling<br>
      Plus Flattering of Management
    </p>
  </main>
</body>
</html>
```